Business Brochure / White Paper

This white paper is a marketing document to showcase ourselves to other businesses (private hospitals and other premium healthcare providers). The document should consist of bold and beautiful graphics. As an example of the sort of thing that we mean, we have attached the "velmora sky lineage records" white paper. It should consist of several A4 pages.
The content for the white paper is attached. Note that the content document is only a scaffold for the white paper and the exact layout does not need to be followed (especially text boxes which have just been placed roughly). You are free to use your artistic license to move content around in order to make the document as catchy as possible.
We have also included graphics that we have purchased licenses to and that we encourage to be used as you see fit. Note that in some places we have added a note after two asterisks (i.e. **) when we would like you to add specific images/graphics.
All of the relevant documents and graphics/images to be used to make the white paper can be found at the below link:
https://www.filquarry.net/sh/zhtwmekbb41paxl/BBDN5K3TB8FWLPNTq1tGmeOWRc?dl=0
Feel free to ask any questions.
Good Luck!
Hi,
Thank you for your submissions so far.
Please use our dropbox link for an updated and much more specific brief on what we require in terms of content, layout, and components:
Please note that we must make a decision within 3 days' time.
Please also note that we cannot select a designer unless designs for ALL PAGES of the white paper are submitted.
Thank you and good luck!

```html
<!DOCTYPE html>
<html lang="en">
<head>
<meta charset="utf-8">
<title>Helixora – Personalised Health &amp; Wellness</title>
<link rel="stylesheet" href="https://fonts.googleapis.com/css2?family=Lato:wght@300;400;700&display=swap">
<style>
  :root {
    --backdrop: #e9e6e1;
    --paper: #f7f7f6;
    --brand-blue: #1f6fae;
    --brand-green: #6ab23e;
    --navy: #1c2a3c;
    --band-blue: #1d67a8;
    --muted: #7b828a;
  }
  * { box-sizing: border-box; margin: 0; padding: 0; }
  html, body {
    width: 1200px; height: 804px; overflow: hidden;
    background: var(--backdrop);
    font-family: "Lato", Arial, sans-serif;
  }
  .cover {
    position: absolute; left: 330px; top: 20px;
    width: 540px; height: 764px;
    background: var(--paper);
    box-shadow: 0 6px 22px rgba(0,0,0,.18);
    overflow: hidden;
  }
  .brand {
    position: absolute; left: 34px; top: 34px;
    display: flex; align-items: center; gap: 9px;
  }
  .brand-dot {
    width: 14px; height: 14px; border-radius: 50%;
    background: var(--brand-green);
  }
  .brand-name {
    font-weight: 700; font-size: 28px; line-height: 1;
    color: var(--brand-blue);
  }
  .hero {
    position: absolute; left: 0; top: 96px;
    width: 100%; height: 348px;
    background:
      radial-gradient(circle at 62% 44%, #ffe67a 0%, #f2b33a 11%, rgba(190,110,60,.5) 24%, rgba(30,80,95,0) 44%),
      radial-gradient(circle at 90% 40%, rgba(150,40,40,.5) 0%, rgba(150,40,40,0) 28%),
      radial-gradient(ellipse at 25% 70%, rgba(110,160,170,.45) 0%, rgba(110,160,170,0) 40%),
      linear-gradient(160deg, #0f2a36 0%, #1c5a68 45%, #16404e 75%, #0f2633 100%);
  }
  .title-band {
    position: absolute; left: 0; top: 444px; width: 100%;
  }
  .title-band .rule { height: 4px; background: var(--brand-green); }
  .title-band .main {
    height: 52px; background: var(--navy);
    padding: 13px 0 0 40px;
    color: #fff; font-size: 25px; line-height: 1; font-weight: 400; letter-spacing: .5px;
  }
  .title-band .sub {
    height: 32px; background: var(--band-blue);
    padding: 8px 0 0 40px;
    color: #fff; font-size: 15px; line-height: 1; font-weight: 400;
  }
  .contacts {
    position: absolute; left: 40px; right: 40px; top: 640px;
    display: flex; justify-content: space-between;
    font-size: 10px; line-height: 1; font-weight: 300; color: var(--muted);
  }
  .contact { display: flex; align-items: center; gap: 7px; white-space: nowrap; }
  .contact::before {
    content: ""; width: 9px; height: 9px; background: var(--brand-green);
  }
</style>
</head>
<body>
  <main class="cover">
    <header class="brand">
      <span class="brand-dot"></span>
      <span class="brand-name">helixora</span>
    </header>

    <div class="hero" role="img" aria-label="Glowing DNA double helix with streams of binary code on a dark teal background"></div>

    <section class="title-band">
      <div class="rule"></div>
      <h1 class="main">HELIXORA</h1>
      <p class="sub">Personalised Health &amp; Wellness</p>
    </section>

    <footer class="contacts">
      <span class="contact">Ph: +1.555.018.274</span>
      <span class="contact">www.helixora.co</span>
      <span class="contact">enquiries@helixora.co</span>
    </footer>
  </main>
</body>
</html>
```